Help keep hoosiers happy and at home!

We need a billboard designed for our Indiana based healthcare business called 'Willow Hearth Caregivers'. We administer a medicaid waiver program that provides support and financial aid to live in caregivers that take care of someone who would otherwise be in a nursing home or skilled nursing facility. Qualified caregivers could be eligible to receive up to 1200 dollars a month in tax free financial aid, as well as access to nursing support that helps manage any unexpected situations or changes in a care recipients condition or care routine. Our program empowers families to keep their loved ones at home and out of the nursing home. NOTE: We believe the tagline at the bottom of our logo is disproportionately small. We would like to see that tagline larger and easier to read. I look forward to seeing your design ideas!

Target Market(s)

Medicaid aged beneficiaries and caregivers.

Industry/Entity Type

Home Healthcare

Colors
0054AA
0677BA
7BADD7
CADEEF
E8F1F8

Requirements
Nice to have
• "Empowering friends and family to care for their loves ones at home. Eligible participants receive up to $15,000 a year, tax free."

```html
<!DOCTYPE html>
<html lang="en">
<head>
<meta charset="utf-8">
<title>Willow Hearth Caregivers Billboard</title>
<link href="https://fonts.googleapis.com/css2?family=Montserrat:wght@600;700;800;900&family=Quicksand:wght@600&display=swap" rel="stylesheet">
<style>
  :root {
    --navy: #1f2a6b;
    --blue: #1b75bb;
    --blue-deep: #0054aa;
    --sky: #cadeef;
    --mist: #e8f1f8;
    --white: #ffffff;
    --ink: #111111;
    --stage: #eef1f4;
  }
  html, body {
    margin: 0;
    padding: 0;
    width: 1200px;
    height: 1200px;
    overflow: hidden;
    background: var(--stage);
  }
  .billboard {
    position: absolute;
    left: 30px;
    top: 430px;
    width: 1140px;
    height: 340px;
    overflow: hidden;
    background: var(--white);
    box-shadow: 0 6px 24px rgba(0,0,0,0.15);
  }
  .photo {
    position: absolute;
    left: 0;
    top: 0;
    width: 380px;
    height: 340px;
    background: linear-gradient(160deg, #7d8a4e 0%, #a08462 40%, #c9a47c 70%, #6f8f45 100%);
  }
  .panel {
    position: absolute;
    left: 0;
    top: 0;
    width: 1140px;
    height: 340px;
  }
  .brand {
    position: absolute;
    left: 290px;
    top: 50px;
    width: 330px;
    text-align: center;
    font-family: 'Quicksand', sans-serif;
  }
  .brand-mark {
    display: block;
    width: 90px;
    height: 90px;
    margin: 0 auto 18px;
    border-radius: 50%;
    background: var(--navy);
  }
  .brand-name {
    margin: 0;
    font-weight: 600;
    font-size: 27px;
    line-height: 1.1;
    color: var(--blue-deep);
  }
  .contact {
    position: absolute;
    left: 290px;
    top: 240px;
    width: 330px;
    font-family: 'Montserrat', sans-serif;
    text-align: center;
  }
  .phone {
    display: flex;
    align-items: center;
    justify-content: center;
    gap: 8px;
    margin: 0;
    font-weight: 800;
    font-size: 34px;
    color: var(--navy);
    letter-spacing: -0.5px;
  }
  .phone svg { width: 24px; height: 24px; }
  .web {
    margin: 4px 0 0;
    font-weight: 600;
    font-size: 14px;
    color: var(--navy);
  }
  .web .domain { color: var(--blue); }
  .message {
    position: absolute;
    left: 650px;
    top: 26px;
    width: 470px;
    font-family: 'Montserrat', sans-serif;
  }
  .lede {
    margin: 0;
    font-weight: 700;
    font-size: 30px;
    line-height: 1.0;
    color: var(--blue);
    text-transform: uppercase;
  }
  .headline {
    margin: 2px 0 0;
    font-weight: 900;
    font-size: 44px;
    line-height: 0.98;
    color: var(--navy);
    text-transform: uppercase;
    letter-spacing: -1px;
  }
  .eligible {
    margin: 16px 0 4px;
    font-weight: 700;
    font-size: 19px;
    color: var(--ink);
    text-transform: uppercase;
  }
  .amount-band {
    margin: 0 -30px 0 0;
    padding: 2px 8px 4px;
    background: var(--blue);
    color: var(--white);
    font-weight: 900;
    font-size: 48px;
    line-height: 1.05;
    letter-spacing: -1px;
  }
  .tax-free {
    margin: 6px 0 0;
    text-align: center;
    font-weight: 900;
    font-size: 26px;
    color: var(--ink);
  }
  .base-strip {
    position: absolute;
    left: 270px;
    bottom: 0;
    width: 870px;
    height: 6px;
    background: var(--navy);
  }
</style>
</head>
<body>
  <div class="billboard">
    <div class="photo" role="img" aria-label="Photo of a smiling woman caring for an elderly man in a wheelchair outdoors"></div>

    <svg class="panel" viewBox="0 0 1140 340" aria-hidden="true">
      <defs>
        <linearGradient id="panelFill" x1="0" y1="0" x2="0" y2="1">
          <stop offset="0" stop-color="#cadeef"/>
          <stop offset="0.55" stop-color="#e8f1f8"/>
          <stop offset="1" stop-color="#ffffff"/>
        </linearGradient>
      </defs>
      <polygon points="272,340 272,128 250,128 380,0 1140,0 1140,340" fill="url(#panelFill)"/>
      <polyline points="272,340 272,128 250,128 380,0" fill="none" stroke="#1f2a6b" stroke-width="4"/>
    </svg>

    <div class="brand">
      <span class="brand-mark"></span>
      <p class="brand-name">Willow Hearth Caregivers</p>
    </div>

    <div class="contact">
      <p class="phone">
        <svg viewBox="0 0 24 24" aria-hidden="true"><path fill="#1f2a6b" d="M6.6 10.8a15.1 15.1 0 0 0 6.6 6.6l2.2-2.2a1 1 0 0 1 1-.25 11.4 11.4 0 0 0 3.6.57 1 1 0 0 1 1 1V20a1 1 0 0 1-1 1A17 17 0 0 1 3 4a1 1 0 0 1 1-1h3.5a1 1 0 0 1 1 1c0 1.25.2 2.45.57 3.57a1 1 0 0 1-.25 1z"/></svg>
        (800)555-0147
      </p>
      <p class="web">www.<span class="domain">willowhearthcaregivers</span>.com</p>
    </div>

    <div class="message">
      <p class="lede">Empowering friends<br>and family to care</p>
      <p class="headline">For their love<br>ones at home</p>
      <p class="eligible">Eligible participants receive up to</p>
      <p class="amount-band">$15,000 A YEAR</p>
      <p class="tax-free">TAX FREE</p>
    </div>

    <div class="base-strip"></div>
  </div>
</body>
</html>
```